Zielgruppe
Wir sind ein Restaurant und starten jetzt mit der Herstellung von eigenen Getränken wie z.B. Whisky, Gin, Rum, Weine, Liköre etc. Die erste Linie des Whiksy haben wir selbst entworfen möchten aber mehr Professionalität einbringen.
Aufgabenstellung
Beiliegend die beiden Flaschen welche bedruckt/beklebt werden (mit Flaschenbezeichnung) und unser LOGO als PSD.
Stichworte: Regional, Qualität, Beste Zutaten, keine Zusatzstoffe
Bezeichnungen: Silberfalter Whisky / Silberfalter Gin
Wichtig: Wiederkennungswert schaffen (Es sollen in Zukunft auch Weine, Liköre etc. produziert werden)
Infos Gin:
- 65 verschiedenen Botanicals
- Neben Blutorangen, Zitronen und Limetten, zeigt auch der Duft von Ingwer, Zitronengras und Kaffirlimettenblätter als Zitrusensemble das Facettenreichtum des Gins. Das Aromaspiel verändert sich nach etwas Zeit im Glas sehr deutlich. Dann zeigen sich starke Aromakomponenten wie Kardamom, Koriander oder Piment. Der Gin zeichnet sich aus durch seine Lebendigkeit
- 42%vol
- 500ml
Infos Whisky:
- 8 Jahre gereift
- Zur Vergärung unseres Whiskys verwenden wir eigens gezüchtete Frischhefe mit besonderen Fähigkeiten zur Bildung von sehr fruchtigen Gäraromen. Die Weichheit bekommt er durch die dreifache Destillation. Auch bei der Wahl unserer Gerste setzen wir auf unsere Region. Der Grund für diesen starken regionalen Bezug ist, dass wir versuchen unserem Whisky die größtmögliche Portion an Terroir zu verleihen. Bei der anschließenden Fasslagerung setzen wir auf hochwertige Fässer. Zuerst neue amerikanische Weißeiche mit anschließendem Sherry- und Cognacfass finish.
Tradition und Moderne verschmelzen zu einem unverwechselbaren Whisky, mit weichem, fruchtigen femininen Geschmack und wildem, maskulinen Charakter.
- Single Malt Whisky
- Geruch & Geschmack: Der Whisky zeichnet sich aus durch intensive, weiche Aromen nach Vanille und süßen Früchten, mit einem ungewöhnlich weichen und sanften Abgang mit einem Hauch von dunkler Schokolade.
Folgende obligatorischen Angaben sind Pflicht:
- Adresse 'Silberfalter / Lindenwiese 7 / 48213 Auenbach-Mühltal'
- Losnummer z.B. L0121..

```html
<!DOCTYPE html>
<html lang="de">
<head>
<meta charset="utf-8">
<title>Silberfalter – Etiketten Gin &amp; Whisky</title>
<link rel="stylesheet" href="https://fonts.googleapis.com/css2?family=Josefin+Sans:wght@400;600&family=Great+Vibes&family=Roboto+Mono:wght@400&family=Roboto+Condensed:wght@400;700&family=Cinzel:wght@400&display=swap">
<style>
:root{
  --bg:#ededed;
  --label:#0c0d10;
  --gold:#c9a233;
  --gold-soft:#9c7d2a;
  --white:#f4f4f4;
  --grey:#b9b9b9;
  --ornament:#3a3b40;
}
*{margin:0;padding:0;box-sizing:border-box}
html,body{width:1200px;height:2313px;overflow:hidden;background:var(--bg)}
.canvas{position:relative;width:1200px;height:2313px;background:linear-gradient(#e4e4e4,#f5f5f5 40%,#e4e4e4 50%,#f5f5f5 90%)}
.label{position:absolute;color:var(--white);text-align:center}
.label-shape{position:absolute;inset:0;width:100%;height:100%}
.label-content{position:absolute;inset:0;display:flex;flex-direction:column;align-items:center}
.brand{display:flex;flex-direction:column;align-items:center;gap:6px}
.brand-dot{border-radius:50%;background:var(--gold)}
.brand-name{font-family:"Josefin Sans",sans-serif;font-weight:600;color:var(--gold);letter-spacing:.04em;line-height:1}
.product{font-family:"Josefin Sans",sans-serif;font-weight:400;letter-spacing:.12em;line-height:1}
.rule{height:1px;background:var(--gold)}
.script-row{position:relative;width:100%;display:flex;justify-content:center}
.script{font-family:"Great Vibes",cursive;color:var(--white);line-height:1.1}
.mono{font-family:"Roboto Mono",monospace;color:var(--grey);letter-spacing:.06em;line-height:1.3}
.edition-block{display:flex;flex-direction:column;align-items:center;gap:4px}
.edition{font-family:"Josefin Sans",sans-serif;letter-spacing:.16em;color:var(--grey);line-height:1}
.ornament{position:absolute;background:var(--ornament);border-radius:40%;opacity:.7}
.gold-flourish{display:block;background:var(--gold-soft);border-radius:40%;opacity:.8}
.specs{position:absolute;left:0;right:0;display:flex;justify-content:space-between;font-family:"Cinzel",serif;color:var(--white);line-height:1}
.specs small{font-size:.6em}
.back-title{font-family:"Josefin Sans",sans-serif;font-weight:600;letter-spacing:.16em;color:var(--white);line-height:1.1}
.back-sub{font-family:"Roboto Condensed",sans-serif;color:var(--gold);line-height:1.3}
.back-copy{font-family:"Roboto Condensed",sans-serif;color:var(--white);line-height:1.3}
.back-copy p{margin-bottom:5px}
.back-copy p:last-child{margin-bottom:0}
.maker{font-family:"Roboto Condensed",sans-serif;color:var(--white);line-height:1.5}
.maker-name{letter-spacing:.16em}
.lot{font-family:"Roboto Condensed",sans-serif;color:var(--white);line-height:1}
.age-badge{position:absolute;top:50%;transform:translateY(-50%);border:1px solid var(--grey);border-radius:50%}
</style>
</head>
<body>
<main class="canvas">

  <!-- Gin front -->
  <section class="label gin-front" style="left:260px;top:517px;width:212px;height:330px">
    <svg class="label-shape" viewBox="0 0 212 330" preserveAspectRatio="none" aria-hidden="true">
      <path d="M0 22 Q106 -8 212 22 V330 H0Z" fill="var(--label)"/>
      <path d="M7 27 Q106 -1 205 27 V323 H7Z" fill="none" stroke="var(--gold)" stroke-width="1"/>
    </svg>
    <div class="ornament" role="img" aria-label="Verziertes Schnörkelornament" style="left:26px;top:31px;width:36px;height:18px"></div>
    <div class="ornament" role="img" aria-label="Verziertes Schnörkelornament" style="right:26px;top:31px;width:36px;height:18px"></div>
    <div class="ornament" role="img" aria-label="Verziertes Schnörkelornament" style="left:22px;top:245px;width:40px;height:20px"></div>
    <div class="ornament" role="img" aria-label="Verziertes Schnörkelornament" style="right:22px;top:245px;width:40px;height:20px"></div>
    <div class="label-content">
      <div class="brand" style="margin-top:34px">
        <span class="brand-dot" style="width:36px;height:36px"></span>
        <span class="brand-name" style="font-size:21px">Silberfalter</span>
      </div>
      <h1 class="product" style="font-size:44px;margin-top:16px">GIN</h1>
      <span class="rule" style="width:40px;margin-top:10px"></span>
      <div class="script-row" style="margin-top:6px"><p class="script" style="font-size:24px">Komposition</p></div>
      <p class="mono" style="font-size:9px;margin-top:2px">aus 65 verschiedenen<br>Botanicals</p>
      <div class="edition-block" style="margin-top:16px">
        <span class="gold-flourish" role="img" aria-label="Goldenes Zierelement" style="width:60px;height:5px"></span>
        <p class="edition" style="font-size:7.5px">LUXURY EDITION</p>
        <span class="gold-flourish" role="img" aria-label="Goldenes Zierelement" style="width:60px;height:5px"></span>
      </div>
    </div>
    <div class="specs" style="bottom:16px;padding:0 16px;font-size:13px"><span>42% <small>VOL</small></span><span>500 <small>ML</small></span></div>
  </section>

  <!-- Gin back -->
  <section class="label gin-back" style="left:755px;top:560px;width:160px;height:248px">
    <svg class="label-shape" viewBox="0 0 160 248" preserveAspectRatio="none" aria-hidden="true">
      <path d="M0 16 Q80 -6 160 16 V248 H0Z" fill="var(--label)"/>
      <path d="M5 20 Q80 -1 155 20 V243 H5Z" fill="none" stroke="var(--gold)" stroke-width="0.8"/>
    </svg>
    <div class="ornament" role="img" aria-label="Verziertes Schnörkelornament" style="left:22px;top:20px;width:22px;height:10px"></div>
    <div class="ornament" role="img" aria-label="Verziertes Schnörkelornament" style="right:22px;top:20px;width:22px;height:10px"></div>
    <div class="label-content">
      <div class="brand" style="margin-top:14px;gap:3px">
        <span class="brand-dot" style="width:15px;height:15px"></span>
        <span class="brand-name" style="font-size:9px">Silberfalter</span>
      </div>
      <h2 class="back-title" style="font-size:9px;margin-top:12px">GIN KOMPOSITION</h2>
      <p class="back-sub" style="font-size:7px">aus 65 verschiedenen Botanicals</p>
      <div class="back-copy" style="font-size:5.6px;margin-top:12px;padding:0 14px">
        <p>Ein facettenreiches Zitrus-Ensemble aus Blutorangen, Zitronen, Limetten und der Duft von Ingwer, Zitronengras und Kaffirlimettenblättern gibt diesem Gin seinen unverkennbaren Geschmack.</p>
        <p>Nach einiger Zeit im Glas beginnt er mit seinem sich verändernden Aromaspiel – ab einem gewissen Moment zeigen sich starke Aromakomponenten wie Kardamom, Koriander und Piment.</p>
        <p>Unser Silberfalter Gin zeichnet sich aus durch seine Lebendigkeit.</p>
      </div>
      <span class="gold-flourish" role="img" aria-label="Goldenes Zierelement" style="width:32px;height:3px;margin-top:9px"></span>
      <div class="maker" style="font-size:5.4px;margin-top:9px">
        <p class="maker-name">SILBERFALTER</p>
        <p>Lindenwiese 7 · 48213 Auenbach-Mühltal</p>
      </div>
      <p class="lot" style="font-size:5.6px;margin-top:10px">L0121</p>
    </div>
  </section>

  <!-- Whisky front -->
  <section class="label whisky-front" style="left:270px;top:1610px;width:189px;height:272px">
    <svg class="label-shape" viewBox="0 0 189 272" preserveAspectRatio="none" aria-hidden="true">
      <path d="M0 18 Q94 -6 189 18 V272 H0Z" fill="var(--label)"/>
      <path d="M6 22 Q94 0 183 22 V266 H6Z" fill="none" stroke="var(--gold)" stroke-width="1"/>
    </svg>
    <div class="ornament" role="img" aria-label="Verziertes Schnörkelornament" style="left:18px;top:24px;width:30px;height:15px"></div>
    <div class="ornament" role="img" aria-label="Verziertes Schnörkelornament" style="right:18px;top:24px;width:30px;height:15px"></div>
    <div class="ornament" role="img" aria-label="Verziertes Schnörkelornament" style="left:16px;top:206px;width:32px;height:16px"></div>
    <div class="ornament" role="img" aria-label="Verziertes Schnörkelornament" style="right:16px;top:206px;width:32px;height:16px"></div>
    <div class="label-content">
      <div class="brand" style="margin-top:24px;gap:5px">
        <span class="brand-dot" style="width:32px;height:32px"></span>
        <span class="brand-name" style="font-size:18px">Silberfalter</span>
      </div>
      <h1 class="product" style="font-size:34px;margin-top:12px;letter-spacing:.08em">WHISKY</h1>
      <span class="rule" style="width:36px;margin-top:8px"></span>
      <div class="script-row" style="margin-top:4px">
        <span class="age-badge" style="left:12px;width:24px;height:24px"></span>
        <p class="script" style="font-size:19px">Single Malt</p>
      </div>
      <p class="mono" style="font-size:7px;margin-top:8px">weich und intensiv zugleich</p>
      <div class="edition-block" style="margin-top:16px">
        <span class="gold-flourish" role="img" aria-label="Goldenes Zierelement" style="width:56px;height:4px"></span>
        <p class="edition" style="font-size:6.5px">LUXURY EDITION</p>
        <span class="gold-flourish" role="img" aria-label="Goldenes Zierelement" style="width:56px;height:4px"></span>
      </div>
    </div>
    <div class="specs" style="bottom:13px;padding:0 12px;font-size:11.5px"><span>42% <small>VOL</small></span><span>500 <small>ML</small></span></div>
  </section>

  <!-- Whisky back -->
  <section class="label whisky-back" style="left:759px;top:1625px;width:161px;height:256px">
    <svg class="label-shape" viewBox="0 0 161 256" preserveAspectRatio="none" aria-hidden="true">
      <path d="M0 16 Q80 -6 161 16 V256 H0Z" fill="var(--label)"/>
      <path d="M5 20 Q80 -1 156 20 V251 H5Z" fill="none" stroke="var(--gold)" stroke-width="0.8"/>
    </svg>
    <div class="ornament" role="img" aria-label="Verziertes Schnörkelornament" style="left:22px;top:22px;width:22px;height:10px"></div>
    <div class="ornament" role="img" aria-label="Verziertes Schnörkelornament" style="right:22px;top:22px;width:22px;height:10px"></div>
    <div class="label-content">
      <div class="brand" style="margin-top:16px;gap:3px">
        <span class="brand-dot" style="width:15px;height:15px"></span>
        <span class="brand-name" style="font-size:9px">Silberfalter</span>
      </div>
      <h2 class="back-title" style="font-size:9px;margin-top:12px">WHISKY</h2>
      <p class="back-sub" style="font-size:7px">Single Malt – 8 Jahre gereift</p>
      <div class="back-copy" style="font-size:5.5px;margin-top:9px;padding:0 12px">
        <p>Regionale Gerste gegärt durch Hilfe eigens gezüchteter Frischhefe, mit besonderen Fähigkeiten zur Bildung von sehr fruchtigen Gäraromen und der anschließenden dreifachen Destillation verdankt dieser Whisky seine unvergleichliche Weichheit und Geschmack.</p>
        <p>Anfangs fassgelagert in hochwertiger amerikanischer Weißeiche, wird dieser Tropfen anschließend veredelt in einem „Sherry- &amp; Cognacfass Finish“.</p>
        <p>Tradition und Moderne verschmelzen zu einem unverwechselbaren Whisky, mit weichem, fruchtigen femininen Geschmack und wildem, maskulinen Charakter.</p>
      </div>
      <span class="gold-flourish" role="img" aria-label="Goldenes Zierelement" style="width:32px;height:3px;margin-top:9px"></span>
      <div class="maker" style="font-size:5.4px;margin-top:8px">
        <p class="maker-name">SILBERFALTER</p>
        <p>Lindenwiese 7 · 48213 Auenbach-Mühltal</p>
      </div>
      <p class="lot" style="font-size:5.6px;margin-top:9px">L0121</p>
    </div>
  </section>

</main>
</body>
</html>
```